Supplement Treats for Dogs and Cats Needs a Label Design

Hello everyone,We are looking for a label design for our new product. We have the container already.Attached you'll find a rough draft of the label we want, along with our logo, and the the animals we would like featured on the label. We will send along the texts, the supplement facts, QPW statement, address, and barcode once as soon as they're ready. For now, we'd like to see a more polished design.Label Measurement: 28cm x 7 cmWe might have some stock photos we want to use, I will attach it later when I have bought them. Please wait before submitting.
MIDDLE AGE

```html
<!DOCTYPE html>
<html lang="en">
<head>
<meta charset="utf-8">
<title>Tails Nova Calming Label</title>
<link rel="stylesheet" href="https://fonts.googleapis.com/css2?family=Fredoka:wght@500;600&family=Roboto:wght@400;700;900&display=swap">
<style>
  :root {
    --bg: #eeeeee;
    --green: #c8e08a;
    --green-light: #d4e79c;
    --orange: #f2a449;
    --orange-deep: #e8933a;
    --silver: #b9bcbf;
    --silver-light: #e3e4e6;
    --label-white: #f7f7f7;
    --brown: #4a2a22;
    --charcoal: #3b3b3d;
    --tag-grey: #a9acb0;
    --photo-dog: #b86a2c;
    --photo-cat: #7d7f86;
  }
  * { margin: 0; padding: 0; box-sizing: border-box; }
  html, body { width: 1200px; height: 800px; overflow: hidden; background: var(--bg); }
  .canvas { position: relative; width: 1200px; height: 800px; }
  .label {
    position: absolute; left: 280px; top: 170px; width: 640px; height: 460px;
    background: var(--label-white); overflow: hidden;
  }
  .label__top {
    position: absolute; left: 0; top: 0; width: 100%; height: 190px;
    background: linear-gradient(90deg, var(--green) 0%, var(--green-light) 50%, var(--green) 100%);
  }
  .brand {
    position: absolute; left: 0; right: 0; top: 40px;
    display: flex; align-items: center; justify-content: center; gap: 14px;
  }
  .brand__dot { width: 22px; height: 22px; border-radius: 50%; background: var(--brown); }
  .brand__name {
    font-family: "Fredoka", sans-serif; font-weight: 600; font-size: 44px;
    letter-spacing: 2px; color: var(--brown);
  }
  .product-name {
    position: absolute; left: 0; right: 0; top: 100px; text-align: center;
    font-family: "Fredoka", sans-serif; font-weight: 600; font-size: 72px;
    line-height: 1; letter-spacing: 2px; color: var(--charcoal);
  }
  .band {
    position: absolute; left: 0; width: 100%;
    background: linear-gradient(180deg, var(--silver-light), var(--silver));
  }
  .band--upper { top: 188px; height: 10px; }
  .band--lower { top: 413px; height: 6px; }
  .label__bottom {
    position: absolute; left: 0; top: 198px; width: 100%; height: 215px;
    background: linear-gradient(90deg, var(--orange-deep) 0%, var(--orange) 50%, var(--orange-deep) 100%);
  }
  .audience {
    position: absolute; left: 0; right: 0; top: 8px; text-align: center;
    font-family: "Fredoka", sans-serif; font-weight: 500; font-size: 25px; color: var(--charcoal);
  }
  .photo {
    position: absolute; left: 143px; top: 44px; width: 320px; height: 160px;
    background: linear-gradient(90deg, var(--photo-dog) 0%, var(--photo-dog) 50%, var(--photo-cat) 75%, rgba(125,127,134,0) 100%);
    border-radius: 70px 60px 8px 8px; opacity: .85;
  }
  .origin-badge {
    position: absolute; left: 52px; top: 148px; width: 64px; height: 46px;
    border-radius: 4px; background: #ffffff; border: 2px solid #c33b3b;
  }
  .count-tag {
    position: absolute; right: 0; top: 142px; width: 190px; height: 56px;
    border-radius: 10px 0 0 10px;
    background: linear-gradient(180deg, #c8cacd, var(--tag-grey));
    display: flex; align-items: center; padding-left: 12px; gap: 6px;
    color: var(--charcoal); font-family: "Roboto", sans-serif;
  }
  .count-tag__number { font-weight: 900; font-size: 36px; }
  .count-tag__text { font-weight: 700; font-size: 13px; line-height: 1.05; text-transform: uppercase; }
  .net-weight {
    position: absolute; left: 0; right: 0; top: 430px; text-align: center;
    font-family: "Roboto", sans-serif; font-weight: 700; font-size: 15px; color: #222222;
  }
</style>
</head>
<body>
<main class="canvas">
  <section class="label">
    <div class="label__top">
      <div class="brand">
        <span class="brand__dot"></span>
        <span class="brand__name">TAILS NOVA</span>
      </div>
      <h1 class="product-name">CALMING</h1>
    </div>
    <div class="band band--upper"></div>
    <div class="label__bottom">
      <p class="audience">For Dogs and Cats</p>
      <div class="photo" role="img" aria-label="Photo of a golden retriever lying down with a grey and white cat nuzzling it"></div>
      <div class="origin-badge" role="img" aria-label="Country of origin badge"></div>
      <div class="count-tag">
        <span class="count-tag__number">60</span>
        <span class="count-tag__text">Soft<br>Chewable<br>Treats</span>
      </div>
    </div>
    <div class="band band--lower"></div>
    <p class="net-weight">Net Weight. 8 oz. (226.8 g.)</p>
  </section>
</main>
</body>
</html>
```